Sales PowerPoint Template to help us attract new customers

We need to create a generic PowerPoint template for our organization. We are in the commercial facilities industry, servicing convenience, restaurants, grocery, and retail customers in the US. We handle trades such as HVAC, Refrigeration, Plumbing, Electrical, Food Equipment, Coffee, etc.

We need to incorporate our new logo, updated colors, Font (Arial). We want it to stand out in this deck and avoid looking like all other facility companies. We want to make sure the template size is not too large (less than 20 MB), so it prevent people to edit/send.
Attached are new logo, colors, old powerpoint template, and finally the "New Design to Incorporate into Template" is new materials we're looking to leverage. This might give you ideas.

Create at least 10 slides (1 cover, 1 agenda slide, at least 7 general slides, and 1 wrap-up slide)

Target Market(s)

Convenience Stores, Retail Stores, Groceries, and Restaurants in the US

Industry/Entity Type

Facilities Services (HVAC, Refrigeration, Plumbing, Electrical, etc, repair and preventative maintenance)

Font styles to use
Other font styles liked:
• Arial

Requirements
Must have
• Follow company colors and font (Arial)
Should not have
• Not approved company colors, font

```html
<!DOCTYPE html>
<html lang="en">
<head>
<meta charset="utf-8">
<title>Norvel Facility Solutions – Sales Template</title>
<link href="https://fonts.googleapis.com/css2?family=Arimo:wght@400;700&display=swap" rel="stylesheet">
<style>
:root{
  --olive:#8b9b3e;
  --olive-dark:#56621f;
  --olive-light:#c9d09e;
  --olive-pale:#e6e9d4;
  --ink:#333333;
  --grey:#8a8a8a;
  --grey-mid:#a9a9a9;
  --grey-light:#dcdcdc;
  --canvas:#dcddd8;
  --dark:#3b3b3b;
  --cream:#ecebe0;
}
*{box-sizing:border-box;margin:0;padding:0}
html,body{width:1200px;height:2951px;overflow:hidden}
body{background:var(--canvas);font-family:"Arimo",Arial,sans-serif;color:var(--ink);position:relative}
.slide{position:absolute;width:510px;height:288px;overflow:hidden;background:#fff}
.col-a{left:77px}.col-b{left:613px}
.abs{position:absolute}
.green-bg{background:var(--olive)}
.dark-bg{background:linear-gradient(135deg,#474747,#2f2f2f)}
.photo{position:absolute}

/* brand text */
.brand{position:absolute;font-weight:700;letter-spacing:4px;font-size:19px;color:var(--ink);display:flex;align-items:center;gap:6px}
.brand i{display:inline-block;width:10px;height:10px;border-radius:50%;background:var(--olive)}
.brand-tag{position:absolute;font-size:8px;color:var(--olive)}

/* footer */
.foot{position:absolute;left:20px;right:20px;bottom:8px;display:flex;align-items:center;font-size:4.5px;color:var(--grey)}
.foot b{font-size:6px;letter-spacing:1.5px;color:var(--olive);margin-right:10px}
.foot .pg{margin-left:auto;font-size:6px}
.foot.light,.foot.light b{color:#fff}
.foot.light{color:rgba(255,255,255,.8)}

/* titles */
.ttl{position:absolute;left:34px;top:22px;font-size:17px;line-height:1.05;color:var(--ink);text-transform:uppercase}
.ttl span{display:block;color:var(--olive)}
.sub{position:absolute;left:34px;top:64px;font-size:6.5px;color:var(--grey)}
.tiny{font-size:5.6px;line-height:1.55;color:var(--grey)}
.lead{font-size:10.5px;line-height:1.1;color:var(--ink)}
ul.bullets{list-style:none;font-size:7.4px;color:var(--ink)}
ul.bullets li{margin-bottom:8px;padding-left:9px;position:relative}
ul.bullets li::before{content:"";position:absolute;left:1px;top:3px;width:3px;height:3px;border-radius:50%;background:var(--ink)}

/* cover */
.cover-title{position:absolute;left:25px;top:118px;font-size:27px;line-height:.93;color:var(--ink)}
.cover-title span{display:block;color:var(--olive)}
.cover-sub{position:absolute;left:25px;top:202px;font-size:8.5px;color:var(--ink)}
.cover-copy{position:absolute;left:25px;top:246px;font-size:6.5px;color:var(--ink)}
.pill{position:absolute;left:415px;top:238px;width:64px;height:22px;border-radius:11px;background:var(--olive);color:#fff;font-size:7.5px;display:flex;align-items:center;justify-content:center}

/* agenda */
.agenda-h{position:absolute;top:42px;width:100%;text-align:center;font-size:20px}
.agenda-h span{color:var(--olive)}
.ag{position:absolute;display:flex;gap:13px;align-items:flex-start}
.ag .num{width:31px;height:31px;border-radius:50%;border:1px solid var(--olive-light);color:var(--olive);font-size:10.5px;display:flex;align-items:center;justify-content:center;margin-top:-4px}
.ag h4{font-weight:400;font-size:11.5px;margin-bottom:5px}
.ag p{font-size:6.8px;color:var(--ink)}

/* section */
.sec-box{position:absolute;left:34px;top:35px;width:232px;height:217px;border:1px solid #e6e6e6}
.sec-num{position:absolute;left:52px;top:66px;font-size:54px;color:var(--olive);line-height:1}
.sec-name{position:absolute;left:52px;top:144px;font-size:22px;line-height:.95}
.sec-name span{display:block;color:var(--olive)}
.sec-txt{position:absolute;left:52px;top:209px;width:130px}

/* three headlines */
.feat{position:absolute;top:132px;width:150px;text-align:center}
.feat svg{display:block;margin:0 auto 6px}
.feat h5{font-weight:400;font-size:9.5px;color:var(--olive);margin-bottom:4px}
.feat p{font-size:6.8px;line-height:1.45;color:#e6e6e6}

/* stats */
.stat{position:absolute;top:106px;display:flex;gap:6px;align-items:flex-start;color:#fff}
.stat b{font-weight:400;font-size:12px;display:block}
.stat p{font-size:6.3px;line-height:1.5;color:rgba(255,255,255,.9)}

/* ring labels */
.lbl{position:absolute;font-size:7.3px;color:var(--ink)}
.seg-n{position:absolute;font-size:9px;color:var(--ink)}

/* quote */
.quote{position:absolute;left:64px;top:106px;font-size:19px;line-height:1.15;color:#fff;width:420px}
.quote-mark{position:absolute;left:25px;top:60px;font-size:110px;line-height:1;color:var(--olive);font-weight:700}

/* four points */
.pt{position:absolute;width:120px}
.pt h3{font-weight:400;font-size:19px;color:var(--olive);margin-bottom:4px}

/* timeline */
.tl-cell{position:absolute;width:113px;text-align:right;padding-right:7px;border-right:1px solid #d8d8d8}
.tl-cell h6{font-weight:400;font-size:12px;color:var(--olive);margin-bottom:3px}

/* descriptions */
.desc{position:absolute;width:120px}
.desc h6{font-weight:400;font-size:9.5px;color:var(--olive);margin-bottom:3px}
.desc.r{text-align:right}

/* promise */
.promise-k{position:absolute;left:141px;top:56px;font-size:9px;color:rgba(255,255,255,.75)}
.promise{position:absolute;left:141px;top:84px;font-size:33px;line-height:1.1;color:#fff}
.promise span{display:block;color:var(--olive-dark)}

.thanks{position:absolute;left:38px;top:140px;font-size:38px;font-weight:700;color:var(--ink)}
.thanks span{color:var(--olive)}
.url{position:absolute;left:38px;top:215px;width:119px;height:21px;background:var(--olive);color:#fff;font-size:8.5px;letter-spacing:.8px;display:flex;align-items:center;justify-content:center;border-radius:2px}
</style>
</head>
<body>

<!-- Row 1: covers -->
<section class="slide col-a" style="top:46px">
  <svg class="abs" width="510" height="288" viewBox="0 0 510 288">
    <path d="M218 0H510V55L418 246Q398 276 378 246Z" fill="var(--cream)"/>
  </svg>
  <div class="photo" role="img" aria-label="Technician in hard hat servicing equipment" style="left:0;top:0;width:510px;height:288px;clip-path:polygon(250px 0,510px 0,510px 40px,410px 232px,392px 240px,380px 228px);background:linear-gradient(150deg,#d8d2b8 0%,#e8c84a 35%,#3c5aa8 60%,#9aa0a8 100%)"></div>
  <div class="brand" style="left:25px;top:35px">NORVEL</div>
  <div class="brand-tag" style="left:46px;top:57px">Facility Solutions</div>
  <h1 class="cover-title" style="font-weight:400">PRESENTATION<br>TITLE TEXT<span>GOES HERE</span></h1>
  <p class="cover-sub">Lorem ipsum dolor sit amet consectetur</p>
  <p class="cover-copy">© Copyright 2025 | Norvel Facility Solutions</p>
  <div class="pill">May 2025</div>
</section>

<section class="slide col-b green-bg" style="top:46px">
  <svg class="abs" width="510" height="288" viewBox="0 0 510 288">
    <path d="M218 0H510V55L418 246Q398 276 378 246Z" fill="var(--cream)"/>
  </svg>
  <div class="photo" role="img" aria-label="Technician in hard hat servicing equipment" style="left:0;top:0;width:510px;height:288px;clip-path:polygon(250px 0,510px 0,510px 40px,410px 232px,392px 240px,380px 228px);background:linear-gradient(150deg,#d8d2b8 0%,#e8c84a 35%,#3c5aa8 60%,#9aa0a8 100%)"></div>
  <div class="brand" style="left:25px;top:35px;color:#fff"><span>NORVEL</span></div>
  <div class="brand-tag" style="left:46px;top:57px;color:#fff">Facility Solutions</div>
  <h1 class="cover-title" style="font-weight:400;color:var(--olive-dark)">PRESENTATION<br>TITLE TEXT<span style="color:#fff">GOES HERE</span></h1>
  <p class="cover-sub" style="color:#fff">Lorem ipsum dolor sit amet consectetur</p>
  <p class="cover-copy" style="color:#fff">© Copyright 2025 | Norvel Facility Solutions</p>
  <div class="pill" style="background:#fff;color:var(--olive)">May 2025</div>
</section>

<!-- Row 2 -->
<section class="slide col-a" style="top:368px">
  <h2 class="agenda-h" style="font-weight:400">OUR <span>AGENDA</span></h2>
  <div class="ag" style="left:34px;top:98px"><div class="num">01</div><div><h4>Subtitle Text Here</h4><p>Lorem ipsum dolor sit amet dummy texts</p></div></div>
  <div class="ag" style="left:34px;top:156px"><div class="num">02</div><div><h4>Subtitle Text Here</h4><p>Lorem ipsum dolor sit amet dummy texts</p></div></div>
  <div class="ag" style="left:34px;top:212px"><div class="num">03</div><div><h4>Subtitle Text Here</h4><p>Lorem ipsum dolor sit amet dummy texts</p></div></div>
  <div class="ag" style="left:264px;top:98px"><div class="num">04</div><div><h4>Subtitle Text Here</h4><p>Lorem ipsum dolor sit amet dummy texts</p></div></div>
  <div class="ag" style="left:264px;top:156px"><div class="num">05</div><div><h4>Subtitle Text Here</h4><p>Lorem ipsum dolor sit amet dummy texts</p></div></div>
  <div class="ag" style="left:264px;top:212px"><div class="num">06</div><div><h4>Subtitle Text Here</h4><p>Lorem ipsum dolor sit amet dummy texts</p></div></div>
  <div class="foot"><b>NORVEL</b>© Copyright 2025 | Norvel Facility Solutions<span class="pg">02</span></div>
</section>

<section class="slide col-b" style="top:368px">
  <h2 class="ttl" style="font-weight:400">Enter your two-line<span>Title here</span></h2>
  <p class="sub">Lorem ipsum dolor sit amet dummy texts.</p>
  <div class="abs green-bg" style="left:0;top:97px;width:183px;height:164px"></div>
  <div class="abs lead" style="left:34px;top:126px;color:#fff;font-size:10px">Lorem ipsum dolor sit<br>amet dummy texts duis</div>
  <p class="abs tiny" style="left:34px;top:151px;width:136px;color:#fff">Lorem ipsum dolor sit amet dummy texts. Duis quis amet nunc vulputate dolor. Scelerisque ligula velit nulla faucibus donec pellentesque massa mi. Aliquam in fusce semper aliquam egestas mauris est nunc. Et pellentesque soda elementum cursus mattis suscipit etiam nulla odio. Molestie tristique cursus ipsum non vitae nibh amet lacus orci dictum erat.</p>
  <div class="photo" role="img" aria-label="Family shopping for fresh produce in a grocery store" style="left:183px;top:97px;width:327px;height:164px;background:linear-gradient(100deg,#c9a36a,#e7d8bf 40%,#7b8f5a 70%,#b2402f)"></div>
  <div class="foot"><b>NORVEL</b>© Copyright 2025 | Norvel Facility Solutions<span class="pg">02</span></div>
</section>

<!-- Row 3: sections -->
<section class="slide col-a" style="top:690px">
  <div class="sec-box"></div>
  <div class="sec-num">01</div>
  <h2 class="sec-name" style="font-weight:400">SECTION<span>SLIDES</span></h2>
  <p class="sec-txt tiny">Lorem ipsum dolor sit amet dummy texts. Duis quis amet nunc vulputate dolor. Scelerisque ligula velit nulla fauci donec.</p>
  <div class="photo" role="img" aria-label="Store worker restocking leafy greens in a refrigerated case" style="left:252px;top:0;width:258px;height:288px;background:linear-gradient(160deg,#e9eef0,#6f9a5a 45%,#2f58b0 75%,#8a6a4a)"></div>
  <div class="foot"><b>NORVEL</b>© Copyright 2025 | Norvel Facility Solutions</div>
</section>

<section class="slide col-b green-bg" style="top:690px">
  <div class="sec-box" style="border-color:rgba(255,255,255,.3)"></div>
  <div class="sec-num" style="color:var(--olive-dark)">02</div>
  <h2 class="sec-name" style="font-weight:400;color:var(--olive-dark)">SECTION<span style="color:#fff">SLIDES</span></h2>
  <p class="sec-txt tiny" style="color:#fff">Lorem ipsum dolor sit amet dummy texts. Duis quis amet nunc vulputate dolor. Scelerisque ligula velit nulla fauci donec.</p>
  <div class="photo" role="img" aria-label="Store worker restocking leafy greens in a refrigerated case" style="left:252px;top:0;width:258px;height:288px;background:linear-gradient(160deg,#e9eef0,#6f9a5a 45%,#2f58b0 75%,#8a6a4a)"></div>
  <div class="foot light"><b>NORVEL</b>© Copyright 2025 | Norvel Facility Solutions<span class="pg">02</span></div>
</section>

<!-- Row 4 -->
<section class="slide col-a dark-bg" style="top:1011px" role="img" aria-label="Darkened store aisle background">
  <h2 class="ttl" style="font-weight:400;left:0;width:100%;text-align:center;top:45px;color:#fff">Enter your two-line<span>Title here</span></h2>
  <p class="sub" style="left:0;width:100%;text-align:center;top:89px;color:#ddd">Lorem ipsum dolor sit amet dummy texts.</p>
  <div class="feat" style="left:26px">
    <svg width="26" height="22" viewBox="0 0 26 22" fill="var(--olive)"><circle cx="13" cy="5" r="4"/><circle cx="5" cy="8" r="3"/><circle cx="21" cy="8" r="3"/><path d="M7 22V15Q13 8 19 15V22Z"/><path d="M0 22V17Q5 11 9 15V22Z"/><path d="M17 22V15Q21 11 26 17V22Z"/></svg>
    <h5>HEADLINE HERE</h5><p>Lorem ipsum dolor sit amet dummy texts. Duis quis amet nunc vulputate dolor scelerisque ligula.</p></div>
  <div class="feat" style="left:180px">
    <svg width="26" height="22" viewBox="0 0 26 22" fill="var(--olive)"><rect x="2" y="14" width="5" height="8"/><rect x="10" y="10" width="5" height="12"/><rect x="18" y="6" width="5" height="16"/><path d="M2 10L10 4 15 7 22 1" stroke="var(--olive)" stroke-width="2" fill="none"/></svg>
    <h5>HEADLINE HERE</h5><p>Lorem ipsum dolor sit amet dummy texts. Duis quis amet nunc vulputate dolor scelerisque ligula.</p></div>
  <div class="feat" style="left:334px">
    <svg width="26" height="22" viewBox="0 0 26 22" fill="var(--olive)"><path d="M0 22L10 9 15 15 18 12 26 22Z"/><rect x="12" y="0" width="1.5" height="11"/><path d="M13.5 0H21L19 3 21 6H13.5Z"/></svg>
    <h5>HEADLINE HERE</h5><p>Lorem ipsum dolor sit amet dummy texts. Duis quis amet nunc vulputate dolor scelerisque ligula.</p></div>
  <div class="foot light"><b>NORVEL</b>© Copyright 2025 | Norvel Facility Solutions<span class="pg">02</span></div>
</section>

<section class="slide col-b" style="top:1011px">
  <h2 class="ttl" style="font-weight:400">Enter your two-line<span>Title here</span></h2>
  <p class="sub">Lorem ipsum dolor sit amet dummy texts.</p>
  <p class="abs" style="left:34px;top:110px;width:140px;font-size:8.5px;line-height:1.6;font-weight:700;color:var(--olive)">Lorem ipsum dolor sit amet dummy texts. Duis quis amet nu vulputate dolor. Sceleri ligula velit nulla faucibus donec pellentesque massa miesat.</p>
  <p class="abs tiny" style="left:206px;top:110px;width:125px;color:var(--ink)">Lorem ipsum dolor sit amet dummy texts. Duis quis amet nunc vulputate dolor. Scelerisque ligula velit nulla fauci donec pellentesque massa mi. Aliquam in fusce semper aliquam egestas mauris est nunc. Et pellentesque sodales elemen tum cursus mattis suscipit etiam.<br><br>Molestie tristique cursus ipsum non vitae nibh amet lacus. Orci dictum erat vitae at at non massa. Sit sit nisl pretium quisque ornare nunc posuere nunc. Et at est varius pulvinar sodales massa pulvinar risus. Orci at ipsum tellus.</p>
  <p class="abs tiny" style="left:347px;top:110px;width:125px;color:var(--ink)">Eget libero aliquet hendrerit et tellus aliquam enim proin elementum. Enim purus nulla nunc accumsan suspen disse gravida dolor nulla. Eget diam elit rhoncus dui integer egestas. Eget sagittis tortor arcu id nec eu integer morbi risus posuere egestas ac.<br><br>Penatibus imperdiet adipiscing rhoncus blandit tortor in. Tortor sagittis massa adipiscing in at nam placerat tincidunt. Ut interdum integer senectus a sapien. Tortor magna velit ut non. Tellus massa etiam vel elementum varius in leo.</p>
  <div class="foot"><b>NORVEL</b>© Copyright 2025 | Norvel Facility Solutions<span class="pg">02</span></div>
</section>

<!-- Row 5 -->
<section class="slide col-a" style="top:1333px">
  <div class="abs green-bg" role="img" aria-label="Hands counting cash, tinted green" style="left:0;top:0;width:510px;height:166px;background:linear-gradient(120deg,#8b9b3e,#9aa84a 60%,#a7b25a)"></div>
  <h2 class="ttl" style="font-weight:400;color:#fff">Enter your two-line<span style="color:#fff">Title here</span></h2>
  <p class="abs tiny" style="left:34px;top:61px;width:190px;color:#fff">Lorem ipsum dolor sit amet dummy texts. Duis quis amet nunc vulputate dolor. Scelerisque ligula velit nulla fauci donec.</p>
  <div class="stat" style="left:47px"><svg width="22" height="18" viewBox="0 0 26 22" fill="#fff"><circle cx="13" cy="5" r="4"/><circle cx="5" cy="8" r="3"/><circle cx="21" cy="8" r="3"/><path d="M7 22V15Q13 8 19 15V22Z"/><path d="M0 22V17Q5 11 9 15V22Z"/><path d="M17 22V15Q21 11 26 17V22Z"/></svg><div><b>10%</b><p>Lorem ipsum dolor sit amet<br>dummy texts duis quis</p></div></div>
  <div class="stat" style="left:200px"><svg width="22" height="18" viewBox="0 0 26 22" fill="#fff"><rect x="2" y="14" width="5" height="8"/><rect x="10" y="10" width="5" height="12"/><rect x="18" y="6" width="5" height="16"/><path d="M2 10L10 4 15 7 22 1" stroke="#fff" stroke-width="2" fill="none"/></svg><div><b>55%</b><p>Lorem ipsum dolor sit amet<br>dummy texts duis quis</p></div></div>
  <div class="stat" style="left:354px"><svg width="22" height="18" viewBox="0 0 26 22" fill="#fff"><path d="M0 22L10 9 15 15 18 12 26 22Z"/><rect x="12" y="0" width="1.5" height="11"/><path d="M13.5 0H21L19 3 21 6H13.5Z"/></svg><div><b>35%</b><p>Lorem ipsum dolor sit amet<br>dummy texts duis quis</p></div></div>
  <div class="abs" style="left:186px;top:104px;width:1px;height:38px;background:rgba(255,255,255,.5)"></div>
  <div class="abs" style="left:340px;top:104px;width:1px;height:38px;background:rgba(255,255,255,.5)"></div>
  <div class="abs lead" style="left:34px;top:189px">Lorem ipsum dolor sit<br>amet dummy texts duis</div>
  <p class="abs tiny" style="left:34px;top:216px;width:120px;color:var(--ink)">Lorem ipsum dolor sit amet dummy texts. Duis quis amet nunc vulputate dolor. Scelerisque ligula velit nulla faucibus donec massa mi.</p>
  <svg class="abs" style="left:172px;top:178px" width="330" height="92" viewBox="0 0 330 92" font-family="Arimo,Arial,sans-serif" font-size="5" fill="var(--ink)">
    <g font-size="4.5"><circle cx="90" cy="6" r="2.5" fill="var(--grey-light)"/><text x="95" y="8">Series 1</text><circle cx="130" cy="6" r="2.5" fill="var(--olive-light)"/><text x="135" y="8">Series 2</text><circle cx="170" cy="6" r="2.5" fill="var(--grey-mid)"/><text x="175" y="8">Series 3</text><circle cx="210" cy="6" r="2.5" fill="var(--olive)"/><text x="215" y="8">Series 4</text></g>
    <text x="0" y="22">20</text><text x="0" y="37">15</text><text x="0" y="52">10</text><text x="2" y="67">5</text><text x="2" y="81">0</text>
    <g>
      <rect x="12" y="63" width="22" height="17" fill="var(--grey-light)"/><rect x="36" y="40" width="22" height="40" fill="var(--olive-light)"/><rect x="60" y="50" width="22" height="30" fill="var(--grey-mid)"/><rect x="84" y="34" width="22" height="46" fill="var(--olive)"/>
      <rect x="118" y="60" width="22" height="20" fill="var(--grey-light)"/><rect x="142" y="34" width="22" height="46" fill="var(--olive-light)"/><rect x="166" y="43" width="22" height="37" fill="var(--grey-mid)"/><rect x="190" y="26" width="22" height="54" fill="var(--olive)"/>
      <rect x="224" y="48" width="22" height="32" fill="var(--grey-light)"/><rect x="248" y="28" width="22" height="52" fill="var(--olive-light)"/><rect x="272" y="40" width="22" height="40" fill="var(--grey-mid)"/><rect x="296" y="22" width="22" height="58" fill="var(--olive)"/>
    </g>
    <line x1="10" y1="80.5" x2="325" y2="80.5" stroke="#ccc" stroke-width=".5"/>
    <text x="52" y="88">Item 1</text><text x="158" y="88">Item 2</text><text x="264" y="88">Item 3</text>
  </svg>
</section>

<section class="slide col-b" style="top:1333px">
  <h2 class="ttl" style="font-weight:400">Enter your two-line<span>Title here</span></h2>
  <p class="sub">Lorem ipsum dolor sit amet dummy texts.</p>
  <div class="photo" role="img" aria-label="Masked cashier serving a customer at a store counter" style="left:0;top:93px;width:246px;height:166px;background:linear-gradient(100deg,#b86a4a,#d9c8b4 35%,#8c6a48 55%,#e2c437 80%,#6c6a68)"></div>
  <div class="abs lead" style="left:266px;top:97px">Lorem ipsum dolor sit<br>amet dummy texts duis</div>
  <p class="abs" style="left:266px;top:125px;width:215px;font-size:6px;line-height:1.5;color:var(--ink)">Lorem ipsum dolor sit amet dummy texts. Duis quis amet nunc vulputate dolor. Scelerisque ligula velit nulla faucibus donec massa mi.</p>
  <ul class="bullets abs" style="left:266px;top:152px">
    <li>Duis quis amet nunc vulputate dolor.</li><li>Scelerisque ligula velit nulla faucibus donec</li><li>Pellentesque massa mi aliquam in fusce</li><li>Semper aliquam egestas mauris est nunc</li><li>Et pellentesque sodales elemenrsus</li><li>Mattis suscipit etiam nulla odio molestie</li>
  </ul>
  <div class="foot"><b>NORVEL</b>© Copyright 2025 | Norvel Facility Solutions<span class="pg">02</span></div>
</section>

<!-- Row 6 -->
<section class="slide col-a" style="top:1655px">
  <h2 class="ttl" style="font-weight:400">Enter your two-line<span>Title here</span></h2>
  <p class="sub">Lorem ipsum dolor sit amet dummy texts.</p>
  <div class="abs lead" style="left:34px;top:106px">Lorem ipsum dolor sit<br>amet dummy texts duis</div>
  <p class="abs tiny" style="left:34px;top:132px;width:210px">Lorem ipsum dolor sit amet dummy texts. Duis quis amet nunc vulputate dolor. Scelerisque ligula velit nulla faucibus donec massa mi.</p>
  <ul class="bullets abs" style="left:34px;top:162px">
    <li>Duis quis amet nunc vulputate dolor.</li><li>Scelerisque ligula velit nulla faucibus donec</li><li>Pellentesque massa mi aliquam in fusce</li><li>Semper aliquam egestas mauris est nunc</li><li>Et pellentesque sodales elemenrsus</li>
  </ul>
  <div class="photo" role="img" aria-label="Two chefs plating a dish in a restaurant kitchen" style="left:262px;top:93px;width:248px;height:166px;background:linear-gradient(110deg,#3a3430,#e9e6e2 35%,#b9b2a8 60%,#2e2a28)"></div>
  <div class="foot"><b>NORVEL</b>© Copyright 2025 | Norvel Facility Solutions<span class="pg">02</span></div>
</section>

<section class="slide col-b" style="top:1655px">
  <h2 class="abs" style="font-weight:400;top:20px;width:100%;text-align:center;font-size:18px">ENTER <span style="color:var(--olive)">TITLE HERE</span></h2>
  <svg class="abs" style="left:0;top:0" width="510" height="288" viewBox="0 0 510 288">
    <g fill="none" stroke-width="55" stroke-dasharray="77 400">
      <circle cx="254" cy="150" r="64.5" stroke="var(--grey-mid)" transform="rotate(-162 254 150)"/>
      <circle cx="254" cy="150" r="64.5" stroke="var(--grey-light)" transform="rotate(-90 254 150)"/>
      <circle cx="254" cy="150" r="64.5" stroke="var(--olive-pale)" transform="rotate(-18 254 150)"/>
      <circle cx="254" cy="150" r="64.5" stroke="var(--olive-light)" transform="rotate(54 254 150)"/>
      <circle cx="254" cy="150" r="64.5" stroke="var(--olive)" transform="rotate(126 254 150)"/>
    </g>
    <g stroke="var(--ink)" stroke-width=".5" fill="none">
      <polyline points="140,64 188,64 208,88"/>
      <polyline points="368,79 330,79 312,98"/>
      <polyline points="120,164 160,164 176,156"/>
      <polyline points="371,210 330,210 316,196"/>
      <polyline points="160,237 190,237 214,214"/>
    </g>
  </svg>
  <div class="seg-n" style="left:214px;top:94px">01</div>
  <div class="seg-n" style="left:289px;top:104px">02</div>
  <div class="seg-n" style="left:309px;top:163px">03</div>
  <div class="seg-n" style="left:237px;top:206px">04</div>
  <div class="seg-n" style="left:181px;top:160px;color:#fff">05</div>
  <div class="abs" style="left:214px;top:137px;width:80px;text-align:center;font-size:10px;line-height:1.15">OUR<br><span style="color:var(--olive)">PRODUCTS</span></div>
  <div class="lbl" style="left:108px;top:60px">HVAC</div>
  <div class="lbl" style="left:372px;top:75px">Refrigeration</div>
  <div class="lbl" style="left:78px;top:155px;text-align:center">Food<br>Equipment</div>
  <div class="lbl" style="left:375px;top:206px">Plumbing</div>
  <div class="lbl" style="left:122px;top:233px">Electrical</div>
  <div class="foot"><b>NORVEL</b>© Copyright 2025 | Norvel Facility Solutions<span class="pg">02</span></div>
</section>

<!-- Row 7 -->
<section class="slide col-a dark-bg" style="top:1977px" role="img" aria-label="Darkened photo of a technician at work">
  <div class="quote-mark">“</div>
  <p class="quote">LOREM IPSUM DOLOR SIT AMET DUMMY TEXTS. DUIS QUIS AMET NUNC VULTATE DOLOR SCELERISQUE LIGULA.</p>
  <div class="abs" style="left:66px;top:203px;width:1.5px;height:18px;background:var(--olive)"></div>
  <div class="abs" style="left:80px;top:210px;font-size:8px;color:var(--olive)">CEO / Founder</div>
</section>

<section class="slide col-b" style="top:1977px">
  <h2 class="ttl" style="font-weight:400">Enter your two-line<span>Title here</span></h2>
  <p class="sub">Lorem ipsum dolor sit amet dummy texts.</p>
  <div class="pt" style="left:38px;top:93px;text-align:center"><h3>01</h3><p class="tiny">Lorem ipsum dolor sit amet dummy texts. Duis quis amet nunc vulputate dolor. Scelerisque ligula velit nulla faucibus donec massa mi.</p></div>
  <div class="pt" style="left:38px;top:183px;text-align:center"><h3>03</h3><p class="tiny">Lorem ipsum dolor sit amet dummy texts. Duis quis amet nunc vulputate dolor. Scelerisque ligula velit nulla faucibus donec massa mi.</p></div>
  <div class="photo" role="img" aria-label="Plumber repairing a kitchen sink faucet" style="left:173px;top:92px;width:165px;height:166px;border-radius:10px;background:linear-gradient(120deg,#e4e2de,#9fb1b4 40%,#2f6468 70%,#cfcac2)"></div>
  <div class="pt" style="left:359px;top:93px"><h3>02</h3><p class="tiny">Lorem ipsum dolor sit amet dummy texts. Duis quis amet nunc vulputate dolor. Scelerisque ligula velit nulla faucibus donec massa mi.</p></div>
  <div class="pt" style="left:359px;top:183px"><h3>04</h3><p class="tiny">Lorem ipsum dolor sit amet dummy texts. Duis quis amet nunc vulputate dolor. Scelerisque ligula velit nulla faucibus donec massa mi.</p></div>
  <div class="foot"><b>NORVEL</b>© Copyright 2025 | Norvel Facility Solutions<span class="pg">02</span></div>
</section>

<!-- Row 8 -->
<section class="slide col-a" style="top:2298px">
  <h2 class="ttl" style="font-weight:400">Enter your two-line<span>Title here</span></h2>
  <p class="sub">Lorem ipsum dolor sit amet dummy texts.</p>
  <div class="tl-cell" style="left:5px;top:120px;height:48px"><h6>2015</h6><p class="tiny">Lorem ipsum dolor sit amet<br>dummy texts duis quis</p></div>
  <div class="tl-cell" style="left:120px;top:120px;height:48px"><h6>2018</h6><p class="tiny">Lorem ipsum dolor sit amet<br>dummy texts duis quis</p></div>
  <div class="tl-cell" style="left:234px;top:120px;height:48px"><h6>2022</h6><p class="tiny">Lorem ipsum dolor sit amet<br>dummy texts duis quis</p></div>
  <div class="tl-cell" style="left:348px;top:120px;height:48px;border-right:0;padding-right:0"><h6>2025</h6><p class="tiny">Lorem ipsum dolor sit amet<br>dummy texts duis quis</p></div>
  <div class="abs" style="left:23px;top:174px;width:458px;height:1px;background:var(--olive)"></div>
  <svg class="abs" style="left:478px;top:169px" width="8" height="11" viewBox="0 0 8 11"><path d="M0 0L8 5.5 0 11Z" fill="var(--olive)"/></svg>
  <div class="tl-cell" style="left:68px;top:180px;height:48px"><h6>2017</h6><p class="tiny">Lorem ipsum dolor sit amet<br>dummy texts duis quis</p></div>
  <div class="tl-cell" style="left:181px;top:180px;height:48px"><h6>2020</h6><p class="tiny">Lorem ipsum dolor sit amet<br>dummy texts duis quis</p></div>
  <div class="tl-cell" style="left:292px;top:180px;height:48px;border-right:0"><h6>2023</h6><p class="tiny">Lorem ipsum dolor sit amet<br>dummy texts duis quis</p></div>
  <div class="foot"><b>NORVEL</b>© Copyright 2025 | Norvel Facility Solutions<span class="pg">02</span></div>
</section>

<section class="slide col-b" style="top:2298px">
  <h2 class="ttl" style="font-weight:400">Enter your two-line<span>Title here</span></h2>
  <p class="sub">Lorem ipsum dolor sit amet dummy texts.</p>
  <svg class="abs" style="left:0;top:0" width="510" height="288" viewBox="0 0 510 288">
    <g fill="none" stroke-width="35">
      <circle cx="256" cy="170" r="51.5" stroke="var(--olive)" stroke-dasharray="126 400" transform="rotate(-90 256 170)"/>
      <circle cx="256" cy="170" r="51.5" stroke="var(--olive-light)" stroke-dasharray="54 400" transform="rotate(50 256 170)"/>
      <circle cx="256" cy="170" r="51.5" stroke="var(--olive-pale)" stroke-dasharray="45 400" transform="rotate(110 256 170)"/>
      <circle cx="256" cy="170" r="51.5" stroke="var(--grey-mid)" stroke-dasharray="36 400" transform="rotate(160 256 170)"/>
      <circle cx="256" cy="170" r="51.5" stroke="var(--grey-light)" stroke-dasharray="36 400" transform="rotate(200 256 170)"/>
      <circle cx="256" cy="170" r="51.5" stroke="#ebebeb" stroke-dasharray="27 400" transform="rotate(240 256 170)"/>
    </g>
  </svg>
  <div class="desc r" style="left:42px;top:104px"><h6>Description Text</h6><p class="tiny">Lorem ipsum dolor sit amet dummy texts duis quis amet nunc vulputate dolor.</p></div>
  <div class="desc r" style="left:42px;top:163px"><h6>Description Text</h6><p class="tiny">Lorem ipsum dolor sit amet dummy texts duis quis amet nunc vulputate dolor.</p></div>
  <div class="desc r" style="left:42px;top:221px"><h6>Description Text</h6><p class="tiny">Lorem ipsum dolor sit amet dummy texts duis quis amet nunc vulputate dolor.</p></div>
  <div class="desc" style="left:351px;top:104px"><h6>Description Text</h6><p class="tiny">Lorem ipsum dolor sit amet dummy texts duis quis amet nunc vulputate dolor.</p></div>
  <div class="desc" style="left:351px;top:163px"><h6>Description Text</h6><p class="tiny">Lorem ipsum dolor sit amet dummy texts duis quis amet nunc vulputate dolor.</p></div>
  <div class="desc" style="left:351px;top:221px"><h6>Description Text</h6><p class="tiny">Lorem ipsum dolor sit amet dummy texts duis quis amet nunc vulputate dolor.</p></div>
</section>

<!-- Row 9 -->
<section class="slide col-a green-bg" style="top:2620px">
  <div class="brand" style="left:430px;top:10px;font-size:12px;letter-spacing:2.5px;color:#fff">NORVEL</div>
  <div class="brand-tag" style="left:452px;top:25px;font-size:5px;color:#fff">Facility Solutions</div>
  <p class="promise-k">OUR PROMISE:</p>
  <p class="promise">Spend less.<br>Strees less.<span>One work order<br>at a time.</span></p>
  <div class="foot light" style="left:14px;right:14px"><span style="font-size:4.5px">© Copyright 2025 | Norvel Facility Solutions</span><span class="pg">02</span></div>
</section>

<section class="slide col-b" style="top:2620px">
  <div class="brand" style="left:37px;top:44px;font-size:21px">NORVEL</div>
  <div class="brand-tag" style="left:72px;top:69px;font-size:8.5px">Facility Solutions</div>
  <h2 class="thanks">THANK <span>YOU</span></h2>
  <div class="url">www.norvelurl.com</div>
</section>

</body>
</html>
```